Business Card Project for Keel Ridge Hoisting

Business name is "Keel Ridge Hoisting" we are a scaffolding & rigging business specialising in local and remote work for:
- scaffolding (residential, commercial, industrial)
- rigging
-man material hoists
- swing stages
- labour hire

On the back of the card I would like KRH as the symbol / logo. I have attached the logos we have had created by pixel harbour. We would like to use bold colours – preferably as the same colour scheme as the logo.

Target Market(s)

Construction business

Industry/Entity Type

Construction

Contact Information for Business Card

name: Miles Fenwick
Title: Director
Phone: 0491 572 846
Address: PO BOX 4821, Ternvale SA 5197
Email: miles@keelridgehoisting.com.au
Website: www.keelridgehoisting.com.au

Font styles to use
Sans Serif

Requirements
Must have
• Must use existing logo & prefering using bold colours
Nice to have
• Would be nice to have a line of dot points in what we specialise in but not essential
• Would be nice to see some designs with a slogan but not essential
Should not have
• NA

```html
<!DOCTYPE html>
<html lang="en">
<head>
<meta charset="utf-8">
<title>Keel Ridge Hoisting – Business Card</title>
<link rel="stylesheet" href="https://fonts.googleapis.com/css2?family=Lato:wght@400;700;900&display=swap">
<style>
  :root {
    --brand-blue: #2c73bf;
    --ink: #151515;
    --paper: #ffffff;
    --backdrop: #e9eaec;
  }
  * { box-sizing: border-box; margin: 0; padding: 0; }
  html, body { width: 1200px; height: 900px; overflow: hidden; }
  body {
    background: var(--backdrop);
    font-family: 'Lato', sans-serif;
    position: relative;
  }
  .card {
    position: absolute;
    left: 250px;
    width: 700px;
    height: 390px;
    overflow: hidden;
    box-shadow: 0 6px 18px rgba(0,0,0,0.18);
  }
  .card-back { top: 40px; background: var(--brand-blue); color: var(--paper); }
  .card-front { top: 470px; background: var(--paper); }

  .back-mark {
    position: absolute;
    left: 0; right: 0; top: 95px;
    text-align: center;
    font-weight: 900;
    font-size: 130px;
    letter-spacing: 6px;
    line-height: 1;
  }
  .service-list {
    position: absolute;
    left: 0; right: 0; top: 262px;
    text-align: center;
    font-size: 19px;
    line-height: 1.4;
  }

  .front-shape { position: absolute; inset: 0; }
  .front-brand {
    position: absolute;
    left: 40px; top: 52px;
    display: flex; align-items: center; gap: 14px;
    font-weight: 900;
    font-size: 34px;
    color: var(--ink);
    letter-spacing: 1px;
  }
  .brand-square { width: 30px; height: 30px; background: var(--brand-blue); }
  .postal-address {
    position: absolute;
    left: 34px; top: 244px;
    color: var(--paper);
    font-size: 19px;
    line-height: 1.35;
  }
  .contact-block {
    position: absolute;
    right: 34px; top: 222px;
    text-align: right;
    color: var(--paper);
  }
  .person-name { font-size: 27px; font-weight: 700; line-height: 1.1; }
  .person-title { font-size: 19px; margin-bottom: 12px; }
  .contact-line {
    display: flex; justify-content: flex-end; align-items: center; gap: 10px;
    font-size: 17px; line-height: 1.45;
  }
  .contact-line svg { width: 16px; height: 16px; flex: none; }
</style>
</head>
<body>

<section class="card card-back">
  <div class="back-mark">KRH</div>
  <div class="service-list">
    <p>scaffolding (residential, commercial, industrial)</p>
    <p>rigging • man material hoists • swing stages • labour hire</p>
  </div>
</section>

<section class="card card-front">
  <svg class="front-shape" viewBox="0 0 700 390" width="700" height="390" aria-hidden="true">
    <defs>
      <clipPath id="swoosh-reach">
        <rect x="300" y="0" width="400" height="390"/>
      </clipPath>
    </defs>
    <path d="M0,180 Q300,300 700,70 L700,390 L0,390 Z" fill="var(--brand-blue)"/>
    <path d="M0,166 Q300,286 700,56" fill="none" stroke="var(--ink)" stroke-width="5" clip-path="url(#swoosh-reach)"/>
  </svg>

  <div class="front-brand">
    <span class="brand-square"></span>
    <span>Keel Ridge Hoisting</span>
  </div>

  <div class="postal-address">
    <p>PO BOX 4821</p>
    <p>Ternvale SA 5197</p>
  </div>

  <div class="contact-block">
    <p class="person-name">Miles Fenwick</p>
    <p class="person-title">Director</p>
    <p class="contact-line">0491 572 846
      <svg viewBox="0 0 24 24" fill="#fff"><path d="M6.6 10.8a15 15 0 0 0 6.6 6.6l2.2-2.2c.3-.3.7-.4 1-.2 1.1.4 2.3.6 3.6.6.6 0 1 .4 1 1V20c0 .6-.4 1-1 1A17 17 0 0 1 3 4c0-.6.4-1 1-1h3.5c.6 0 1 .4 1 1 0 1.3.2 2.5.6 3.6.1.3 0 .7-.2 1z"/></svg>
    </p>
    <p class="contact-line">miles@keelridgehoisting.com.au
      <svg viewBox="0 0 24 24" fill="none" stroke="#fff" stroke-width="2"><rect x="3" y="5" width="18" height="14"/><path d="M3 5l9 8 9-8"/></svg>
    </p>
    <p class="contact-line">www.keelridgehoisting.com.au
      <svg viewBox="0 0 24 24" fill="none" stroke="#fff" stroke-width="2"><circle cx="12" cy="12" r="9"/><path d="M3 12h18M12 3c3 3 3 15 0 18M12 3c-3 3-3 15 0 18"/></svg>
    </p>
  </div>
</section>

</body>
</html>
```